Flyer-Design für IT Support
Zielgruppe
Ich bin spezialisiert auf IT Support für Private Anwender die PC Probleme haben hat bis hin zu kleinen Unternehmen, die keine eigene IT besitzen. Bei kleinen Unternehmen betreue ich das Netzwerk sowie Server.
Aufgabenstellung
Es soll der Support und Verkauf von PCs/Laptops angeboten werden. Mit ansprechenden Texten zum Verkauf von Leistungen und Produkten.

```html
<!DOCTYPE html>
<html lang="de">
<head>
<meta charset="utf-8">
<title>Halverk-IT – Flyer</title>
<link href="https://fonts.googleapis.com/css2?family=Open+Sans:wght@400;700&display=swap" rel="stylesheet">
<style>
  :root {
    --navy: #0b4670;
    --blue: #0d66a6;
    --blue-bright: #0e6fae;
    --sky: #e7f3fb;
    --white: #ffffff;
    --label-grey: #9a9a9a;
  }
  html, body {
    margin: 0;
    padding: 0;
    width: 1200px;
    height: 900px;
    overflow: hidden;
    background: var(--white);
    font-family: "Open Sans", Arial, sans-serif;
  }
  .canvas { position: relative; width: 1200px; height: 900px; }
  .side-label {
    position: absolute;
    top: 94px;
    width: 200px;
    margin-left: -100px;
    text-align: center;
    color: var(--label-grey);
    font-size: 15px;
  }
  .side-label--back { left: 388px; }
  .side-label--front { left: 824px; }

  .flyer {
    position: absolute;
    left: 163px;
    top: 141px;
    width: 888px;
    height: 630px;
    box-shadow: 4px 6px 14px rgba(0,0,0,0.28);
    overflow: hidden;
  }
  .flyer__shapes { position: absolute; inset: 0; }

  .brand {
    position: absolute;
    top: 30px;
    width: 160px;
    margin-left: -80px;
    text-align: center;
    color: var(--blue);
  }
  .brand__dot {
    display: block;
    width: 32px;
    height: 32px;
    margin: 0 auto 6px;
    border-radius: 50%;
    background: var(--blue);
  }
  .brand__name { font-size: 21px; font-weight: 400; line-height: 1; }
  .brand--back { left: 352px; }
  .brand--front { left: 534px; }

  .back-copy {
    position: absolute;
    left: 0;
    width: 444px;
    color: var(--white);
    text-align: center;
  }
  .back-copy__title {
    top: 183px;
    font-size: 16px;
    font-weight: 700;
    margin: 0;
  }
  .back-copy__intro {
    top: 219px;
    font-size: 13px;
    line-height: 17.4px;
    margin: 0;
  }
  .back-copy__services-title {
    top: 324px;
    font-size: 13px;
    font-weight: 700;
    margin: 0;
  }
  .service {
    position: absolute;
    left: 0;
    width: 444px;
    text-align: center;
    color: var(--white);
    font-size: 13px;
  }
  .contact {
    position: absolute;
    left: 0;
    width: 444px;
    top: 572px;
    text-align: center;
    color: var(--white);
    font-size: 10.5px;
    line-height: 15.5px;
  }

  .badge {
    position: absolute;
    left: 651px;
    top: 390px;
    width: 206px;
    height: 206px;
    border-radius: 50%;
    background: var(--white);
    box-shadow: 0 2px 8px rgba(0,0,0,0.2);
  }
  .badge__ring {
    position: absolute;
    inset: 8px;
    border: 3px solid var(--blue);
    border-radius: 50%;
    display: flex;
    align-items: center;
    justify-content: center;
    text-align: center;
    color: var(--blue);
    font-weight: 700;
    font-size: 25px;
    line-height: 28px;
  }
  .front-url {
    position: absolute;
    left: 504px;
    width: 200px;
    top: 585px;
    text-align: center;
    color: var(--white);
    font-size: 13px;
  }
</style>
</head>
<body>
<div class="canvas">
  <div class="side-label side-label--back">Rückseite</div>
  <div class="side-label side-label--front">Vorderseite</div>

  <div class="flyer">
    <svg class="flyer__shapes" width="888" height="630" viewBox="0 0 888 630">
      <defs>
        <radialGradient id="backGradient" cx="0.95" cy="0.55" r="0.9">
          <stop offset="0" stop-color="#0e6fae"/>
          <stop offset="1" stop-color="#0b4670"/>
        </radialGradient>
        <linearGradient id="frontBandGradient" x1="0" y1="0" x2="1" y2="0">
          <stop offset="0" stop-color="#0e6fae"/>
          <stop offset="1" stop-color="#0b4670"/>
        </linearGradient>
        <radialGradient id="photoGradient" cx="0.5" cy="0.45" r="0.6">
          <stop offset="0" stop-color="#d9d2cc"/>
          <stop offset="0.6" stop-color="#c9b8a8"/>
          <stop offset="1" stop-color="#e7f3fb"/>
        </radialGradient>
      </defs>
      <rect class="paper" width="888" height="630" fill="var(--white)"/>
      <polygon class="back-panel" points="0,0 105,0 444,187 444,630 0,630" fill="url(#backGradient)"/>
      <polygon class="front-panel" points="444,187 783,0 888,0 888,630 444,630" fill="var(--sky)"/>
      <rect class="front-photo" role="img" aria-label="Foto: Mann mit Kapitänsmütze und Pfeife zeigt mit beiden Händen das OK-Zeichen" x="471" y="98" width="397" height="434" rx="60" fill="url(#photoGradient)"/>
      <polygon class="front-band-white" points="444,580 888,410 888,426 444,597" fill="var(--white)"/>
      <polygon class="front-band" points="444,597 888,426 888,630 444,630" fill="url(#frontBandGradient)"/>
      <g class="service-connectors" stroke="var(--white)" stroke-width="1" stroke-dasharray="2 2">
        <line x1="222" y1="344" x2="222" y2="357"/>
        <line x1="222" y1="378" x2="222" y2="409"/>
        <line x1="222" y1="430" x2="222" y2="461"/>
        <line x1="222" y1="482" x2="222" y2="513"/>
      </g>
      <line class="back-divider" x1="31" y1="556" x2="415" y2="556" stroke="var(--white)" stroke-width="1"/>
    </svg>

    <div class="brand brand--back"><span class="brand__dot"></span><span class="brand__name">Halverk-IT</span></div>
    <div class="brand brand--front"><span class="brand__dot"></span><span class="brand__name">Halverk-IT</span></div>

    <h2 class="back-copy back-copy__title" style="position:absolute">SIE BRAUCHEN HILFE?</h2>
    <p class="back-copy back-copy__intro" style="position:absolute">
      Kein Problem... wir sind spezialisiert auf IT Support für Private<br>
      Anwender die PC Probleme haben bis hin zu kleinen<br>
      Unternehmen, die keine eigene IT besitzen.<br>
      Bei kleinen Unternehmen betreue ich das<br>
      Netzwerk sowie Server.
    </p>
    <p class="back-copy back-copy__services-title" style="position:absolute">Folgende Dienstleistungen bieten wir an:</p>
    <div class="service" style="top:358px">Microsoft</div>
    <div class="service" style="top:410px">Netzwerk</div>
    <div class="service" style="top:462px">Sicherheit</div>
    <div class="service" style="top:514px">Hardware</div>

    <div class="contact">
      J. Halverk | IT-Berater | Möwenweg 8 | 23970 Wismar<br>
      Telefon: 0176 24589031 | kontakt@halverk-it.de &nbsp;| www.halverk-it.de
    </div>

    <div class="badge"><div class="badge__ring">IT BERATUNG<br>IM NORDEN</div></div>
    <div class="front-url">www.halverk-it.de</div>
  </div>
</div>
</body>
</html>
```